Business cards

Dog breeder selling very high end expensive pets so design must be modern, simple (with the focus being on the photos) and upscale. Would like a full photo on each side of the card with text as an accent more then as the focus.
I would like the name of the business to be large and bold (possibly modern cursive font) and centered preferably but am open to other options
Need the French bulldogs on the front if the card if not both. I was thinking of one full photo on each side but as long as the French Bulldogs are the focus I'm open to all options. The French bulldogs are the ones in the photo with three puppies pictured
Info needed on the card:
Velvet Pawhouse
www.velvetpawhouse-demo.net
thevelvetpawhouse@postvine-mail.net
(702) 555-0148
On the back:
Quality pets and champion show dogs

```html
<!DOCTYPE html>
<html lang="en">
<head>
<meta charset="utf-8">
<title>Velvet Pawhouse – Business Card</title>
<link rel="stylesheet" href="https://fonts.googleapis.com/css2?family=Advent+Pro:wght@400&family=Lato:wght@400&display=swap">
<style>
  :root {
    --page-bg: #ffffff;
    --ink-teal: #1e3a40;
    --text-light: #f4f1e6;
    --card-deep: #4b6b5c;
    --card-sage: #a3ae80;
    --card-cream: #f3e498;
    --card-shadow-edge: #6b6a52;
    --photo-warm: #d9c48f;
    --photo-brown: #9a6a45;
  }
  * { box-sizing: border-box; margin: 0; padding: 0; }
  html, body {
    width: 1200px;
    height: 1000px;
    overflow: hidden;
    background: var(--page-bg);
  }
  .business-card {
    position: absolute;
    left: 57px;
    top: 181px;
    width: 1086px;
    height: 638px;
    border-radius: 60px;
    overflow: hidden;
    background:
      radial-gradient(ellipse 70% 80% at 100% 55%, var(--card-cream) 0%, rgba(243,228,152,0) 70%),
      linear-gradient(180deg, rgba(0,0,0,0) 80%, rgba(90,88,66,0.45) 100%),
      linear-gradient(125deg, var(--card-deep) 0%, var(--card-sage) 35%, #d6cf92 65%, var(--card-cream) 100%);
  }
  .brand-name {
    position: absolute;
    left: 0;
    right: 0;
    top: 178px;
    text-align: center;
    font-family: "Advent Pro", sans-serif;
    font-weight: 400;
    font-size: 82px;
    line-height: 1;
    letter-spacing: 1px;
    color: var(--ink-teal);
    transform: translateX(2px);
  }
  .contact-panel {
    position: absolute;
    left: 0;
    top: 382px;
    width: 556px;
    height: 199px;
    background: var(--ink-teal);
    border-radius: 0 28px 28px 0;
    padding: 25px 42px 0 0;
    text-align: right;
    font-family: "Lato", sans-serif;
    font-size: 27px;
    line-height: 53px;
    color: var(--text-light);
  }
  .contact-line { display: block; white-space: nowrap; }
  .puppy-photo {
    position: absolute;
    left: 585px;
    top: 352px;
    width: 501px;
    height: 286px;
    background:
      radial-gradient(ellipse 55% 45% at 72% 62%, rgba(154,106,69,0.55) 0%, rgba(154,106,69,0) 100%),
      radial-gradient(ellipse 40% 40% at 42% 35%, rgba(240,230,210,0.7) 0%, rgba(240,230,210,0) 100%),
      linear-gradient(180deg, rgba(217,196,143,0) 0%, var(--photo-warm) 100%);
  }
</style>
</head>
<body>
  <div class="business-card">
    <h1 class="brand-name">Velvet Pawhouse</h1>
    <div class="contact-panel">
      <span class="contact-line">www.velvetpawhouse-demo.net</span>
      <span class="contact-line">thevelvetpawhouse@postvine-mail.net</span>
      <span class="contact-line">(702) 555-0148</span>
    </div>
    <div class="puppy-photo" role="img" aria-label="Photo of a bulldog puppy resting its chin on a patterned food bowl piled with kibble"></div>
  </div>
</body>
</html>
```